"Every Lantern Still Burning" Sermon Series Design

Needing a design for our church's next sermon series titled "Every Lantern Still Burning" where we will discuss the need for unity, diversity, love and clarity. Looking for a 1920 x 1080 (or higher res) editable and layered file (PSD or AI) so that we can reformat the design to work on social, screens, lower thirds and various print and online mediums. We will also need to have access to the font files so that we can make resize and tweak as needed. We like the idea of using a globe or map of the world as the backdrop with the words overtop. Or, the idea of creating a bunch of newspaper clippings (generic, so that they can't actually be read) and making the shape of a heart. See attached examples. This website will give you an idea of our previous sermon series designs so you can have an idea of our style (but, feel free to help us advance the ball on something more aligned with current design trends): https://www.brinmoorfellowship.church/series

Examples use red, but stay away from a ton of red. If you're gonna major in a color, use blue or something in that family.

Must haves:
Title: Every Lantern Still Burning
Tagline : (TBD - use some Lorem Ipsum as a placeholder and we will fill in later)
Our Logo (attached) (small towards bottom is standard - only use solid colors for logo - preferably just solid black or white)

Industry/Entity Type

Church

Font styles to use
Serif
Sans Serif

Requirements
Must have
• Title: Every Lantern Still Burning
Nice to have
• We like the idea of using a globe or map of the world as the backdrop with the words overtop. Or, the idea of creating a bunch of newspaper clippings (generic, so that they can't actually be read) and making the shape of a heart. See attached examples.

If you're gonna major on a color, stick with blue or something close.
Should not have
• Don't use red as the primary color (example we sent has red, but stay away from it)

```html
<!DOCTYPE html>
<html lang="en">
<head>
<meta charset="UTF-8">
<title>Every Lantern Still Burning – Sermon Series</title>
<link href="https://fonts.googleapis.com/css2?family=Raleway:wght@500;600&display=swap" rel="stylesheet">
<style>
  :root {
    --sky-top: #1560a0;
    --sky-mid: #3a9fe0;
    --sky-low: #7fcaf2;
    --sky-bottom: #c4e9fa;
    --cloud: rgba(240, 248, 255, 0.92);
    --ink: #0b4d78;
  }
  * { margin: 0; padding: 0; box-sizing: border-box; }
  html, body {
    width: 1200px;
    height: 675px;
    overflow: hidden;
  }
  body {
    font-family: "Raleway", sans-serif;
    color: var(--ink);
  }
  .series-slide {
    position: relative;
    width: 1200px;
    height: 675px;
    overflow: hidden;
  }
  .sky-backdrop {
    position: absolute;
    inset: 0;
    background:
      radial-gradient(ellipse 270px 250px at 600px 300px, var(--cloud) 0%, rgba(230, 244, 255, 0.75) 45%, rgba(220, 240, 255, 0) 100%),
      linear-gradient(180deg, var(--sky-top) 0%, #1e7cc4 22%, var(--sky-mid) 45%, var(--sky-low) 72%, var(--sky-bottom) 100%);
  }
  .series-title {
    position: absolute;
    top: 186px;
    left: 0;
    width: 100%;
    text-align: center;
    font-weight: 600;
    font-size: 40px;
    line-height: 66px;
    letter-spacing: 0.55em;
    text-transform: uppercase;
  }
  .series-title span {
    display: block;
    padding-left: 0.55em;
  }
  .series-tagline {
    position: absolute;
    top: 594px;
    left: 290px;
    width: 630px;
    text-align: center;
    font-weight: 500;
    font-size: 12.2px;
    line-height: 15px;
  }
</style>
</head>
<body>
  <main class="series-slide">
    <div class="sky-backdrop" role="img" aria-label="Bright blue sky with a soft white heart-shaped cloud in the centre"></div>

    <h1 class="series-title">
      <span>Every</span>
      <span>Lantern</span>
      <span>Still</span>
      <span>Burning</span>
    </h1>

    <p class="series-tagline">Lorem Ipsum is simply dummy text of the printing and typesetting industry. Lorem Ipsum has been the industry's standard dummy text ever since the 1500s, when an unknown printer took a galley of type and scrambled it to make a type specimen book</p>
  </main>
</body>
</html>
```